Label Redesign For Hemp Oil Tincture Bottle*

I need a label redesigned for Meadowlark Botanics, current bottle label and logo is attached. The current label doesn't standout, not sure if its the font size or colors on the existing label. It is very important to have on the label that this is a Premium Full Spectrum Hemp Oil that is 2000mg. Then after the label is redesigned and approved, I would need to packaging to be designed to match the approved label design.
This Hemp oil has a relaxing effect to help ease mental and emotional stress, tension and worry. The Omega Fatty Acids it contains also naturally improves your mood and overall brain function, causing you to feel more alert and focused. Hemp Oil helps with insomnia. Take some 2-3 hours before bedtime, you will feel relaxed yet aware of how tired you are that it will lead to a good night's sleep. Hemp Oil helps ease chronic pain and inflammation from conditions such as arthritis, fibromyalgia, lupus, and MS. As a pain relief supplement, it is a safer, natural, non-chemical and non-addictive alternative to prescription painkillers.
Updates

Target Market(s)

Adults

Industry/Entity Type

Supplement

Font styles to use
Serif
Sans Serif

Colors

Designer to choose colors to be used in the design.

Requirements
Must have
• All information thats on current label but where it says 750 in the front of the existing label, it needs to say 2000. The 2000 should be prominent on the label.

```html
<!DOCTYPE html>
<html lang="en">
<head>
<meta charset="utf-8">
<title>Meadowlark Botanics – Hemp Oil Label</title>
<link href="https://fonts.googleapis.com/css2?family=Josefin+Sans:wght@300&family=Titillium+Web:wght@400;600;700&display=swap" rel="stylesheet">
<style>
  :root {
    --bg: #f4f5f3;
    --label: #ffffff;
    --green: #4c8f2b;
    --green-dark: #3b7a20;
    --green-light: #9cc286;
    --ink: #3a3a3a;
    --teal: #1ca6a6;
  }
  html, body {
    margin: 0;
    padding: 0;
    width: 1200px;
    height: 1200px;
    overflow: hidden;
    background: var(--bg);
  }
  .label {
    position: absolute;
    left: 240px;
    top: 50px;
    width: 720px;
    height: 1100px;
    background: var(--label);
    border-top: 10px solid var(--green);
    border-bottom: 10px solid var(--green);
    box-sizing: border-box;
    font-family: "Titillium Web", sans-serif;
    text-align: center;
  }
  .brand {
    position: absolute;
    top: 52px;
    left: 0;
    right: 0;
    display: flex;
    justify-content: center;
    align-items: center;
    gap: 22px;
  }
  .brand-mark {
    width: 70px;
    height: 70px;
    border-radius: 50%;
    background: var(--green);
  }
  .brand-text {
    text-align: left;
    line-height: 1.05;
  }
  .brand-name {
    font-weight: 600;
    font-size: 34px;
    color: var(--ink);
    text-transform: uppercase;
  }
  .brand-tag {
    font-weight: 400;
    font-size: 30px;
    color: var(--green);
    margin-top: 6px;
  }
  .band {
    position: absolute;
    top: 222px;
    left: 0;
    right: 0;
    height: 62px;
    background: linear-gradient(180deg, var(--green) 0%, var(--green-dark) 100%);
    color: #fff;
    font-size: 40px;
    font-weight: 400;
    line-height: 62px;
    letter-spacing: 0.5px;
  }
  .strength {
    position: absolute;
    top: 310px;
    left: 0;
    right: 0;
    font-family: "Josefin Sans", sans-serif;
    font-weight: 300;
    font-size: 96px;
    letter-spacing: 16px;
    color: var(--green);
    line-height: 1;
  }
  .drop {
    position: absolute;
    top: 430px;
    left: 255px;
    width: 210px;
    height: 330px;
  }
  .product-name {
    position: absolute;
    top: 780px;
    left: 0;
    right: 0;
    margin: 0;
    font-size: 132px;
    font-weight: 700;
    line-height: 140px;
    color: var(--green);
    letter-spacing: -2px;
  }
  .supplement {
    position: absolute;
    top: 935px;
    left: 0;
    right: 0;
    font-size: 38px;
    letter-spacing: 7px;
    color: var(--ink);
    line-height: 1;
  }
  .flavor {
    position: absolute;
    top: 985px;
    left: 0;
    right: 0;
    font-size: 34px;
    color: var(--teal);
    line-height: 1;
  }
  .volume {
    position: absolute;
    top: 1032px;
    left: 0;
    right: 0;
    font-size: 30px;
    font-weight: 700;
    color: var(--ink);
    line-height: 1;
  }
</style>
</head>
<body>
  <main class="label">
    <header class="brand">
      <div class="brand-mark"></div>
      <div class="brand-text">
        <div class="brand-name">Meadowlark Botanics</div>
        <div class="brand-tag">ZERO THC</div>
      </div>
    </header>

    <div class="band">PREMIUM FULL SPECTRUM</div>
    <div class="strength">2000MG</div>

    <svg class="drop" viewBox="0 0 210 330" role="img" aria-label="Faceted green oil drop graphic">
      <defs>
        <linearGradient id="dropFill" x1="0" y1="0" x2="1" y2="1">
          <stop offset="0" stop-color="#9cc286"/>
          <stop offset="1" stop-color="#3f7f25"/>
        </linearGradient>
      </defs>
      <path d="M105 0 C140 70 210 150 210 225 A105 105 0 0 1 0 225 C0 150 70 70 105 0 Z" fill="url(#dropFill)"/>
    </svg>

    <h1 class="product-name">HEMP OIL</h1>

    <div class="supplement">DIETARY SUPPLIMENT</div>
    <div class="flavor">NATURAL PEPPERMINT FLAVOR</div>
    <div class="volume">1FL.OZ (30ML)</div>
  </main>
</body>
</html>
```